42crt.com - International Brand Needs A Fresh Look

New Company needing an fresh clean look. 42crts.com.au

Product: SSLs

Brands: Varnolux, TerraBond, Plimmo, SwiftCRT

Encourage all designers that can deliver a clean and fresh design with a touch of imagination.

We don't want this to be your typical boring ssl reseller site, we want the whole process to be fast and transparent. We welcome your design ideas.

Unrelated site designs we like:
www.wideshopfront.com, www.plorvix.com

Backend - Orlisk Run

Pages to design:

Home Page - see examples above. looking for fresh ideas!!

Product Page - try and avoid grids or boring/usual ways to display ssl information and product info. looking for fresh ideas!!

Contact us page

Checkout - using orlisk run, so not sure how much we can customise on this page

we had thought about an idea using an input box on the home page - that looks like a browser bar where they enter the url they are purchasing for - different way to display this and get them to interact with the site. when they click find SSLs button the options display below.... just a thought!

Please ask any questions you have.

Thanks.
Marcus

Requirements
Must have
• logos of the brands we are selling and we are platinum partners of each.

logo's of brands that use our ssls - please choose some example ones.

Nice to have
• nice to have a most popular either for each one or across the site

```html
<!DOCTYPE html>
<html lang="en">
<head>
<meta charset="utf-8">
<title>42crt – Protect Your Website &amp; Grow Your Business</title>
<link href="https://fonts.googleapis.com/css2?family=Nunito:wght@400;600;700;800&family=Arimo:wght@400;700&display=swap" rel="stylesheet">
<style>
:root{
  --header-dark:#3c3c3c;
  --nav-grey:#cfcfcf;
  --sky:#4ac3e5;
  --ocean:#0fa4cf;
  --mint:#00c686;
  --amber:#e89a2a;
  --lime:#7cc52e;
  --lime-dark:#5ea61c;
  --red:#c3282d;
  --sun:#ffe23b;
  --ink:#222;
  --paper:#fff;
  --logo-strip:#f3f3f3;
  --footer:#4a4a4a;
  --head-font:"Nunito",sans-serif;
  --body-font:"Arimo",sans-serif;
}
*{box-sizing:border-box;margin:0;padding:0}
html,body{width:1200px;height:3165px;overflow:hidden}
body{font-family:var(--body-font);color:var(--ink);background:var(--paper);position:relative}
.abs{position:absolute}

/* top bar */
.topbar{top:0;left:0;width:1200px;height:58px;background:var(--header-dark)}
.brand{font-family:var(--head-font);font-weight:800;color:#fff;font-size:36px;left:153px;top:6px;letter-spacing:-1px}
.live-chat{left:556px;top:18px;color:#fff;font-size:17px}
.region{left:678px;top:22px;color:#ddd;font-size:12px}
.search{left:786px;top:18px;width:242px;height:22px;background:#fff;border-radius:2px}
.search svg{position:absolute;right:6px;top:4px}

.navbar{top:58px;left:0;width:1200px;height:61px;background:var(--nav-grey)}
.navbar ul{list-style:none;display:flex;gap:44px;position:absolute;right:172px;top:20px}
.navbar li{font-size:17px;color:#333}

/* hero */
.hero-title{top:226px;left:0;width:1200px;text-align:center;font-family:var(--head-font);font-weight:600;color:var(--sky);font-size:72px;line-height:80px;letter-spacing:-1px}
.hero-sub{top:402px;left:0;width:1200px;text-align:center;font-family:var(--head-font);font-size:29px;line-height:40px;color:#333}
.url-input{left:256px;top:527px;width:477px;height:64px;background:#e6e6e6;border:2px solid #cfcfcf;border-radius:8px;font-size:21px;color:#888;padding:19px 26px}
.find-btn{left:746px;top:527px;width:198px;height:64px;background:linear-gradient(var(--lime),var(--lime-dark));border-radius:8px;color:#fff;font-size:21px;text-align:center;line-height:64px}

/* why */
.why{top:707px;left:0;width:1200px;height:469px;background:var(--sky);color:#fff}
.why h2{position:absolute;top:80px;width:100%;text-align:center;font-family:var(--head-font);font-weight:800;font-size:74px;letter-spacing:-1px}
.feature{position:absolute;top:205px;width:330px;text-align:center}
.feature svg{display:block;margin:0 auto 22px}
.feature h3{font-family:var(--head-font);font-weight:700;font-size:25px;color:#183848;margin-bottom:12px}
.feature p{font-size:16px;line-height:21px;color:#1e4656}

/* trial */
.trial-photo{left:250px;top:1292px;width:304px;height:414px;background:linear-gradient(180deg,#e9e4df 0%,#cbd6b8 55%,#8cc35a 100%)}
.trial-sign{left:145px;top:1210px;width:200px;height:150px;background:var(--mint);border-radius:20px;transform:rotate(-6deg);color:#fff;font-family:var(--head-font);font-weight:800;padding:22px 16px;white-space:nowrap;line-height:1.15}
.trial-sign .s1{font-size:19px}
.trial-sign .s2{font-size:27px;color:var(--sun)}
.trial-sign .s3{font-size:15px}
.trial-copy{left:622px;top:1298px;width:400px}
.trial-copy h2{font-family:var(--head-font);font-weight:800;color:var(--red);font-size:37px;margin-bottom:20px}
.trial-copy h3{font-size:21px;font-weight:700;margin-bottom:14px}
.trial-copy p{font-size:16.5px;line-height:23px;color:#333;margin-bottom:22px}

/* plans */
.plans{top:1706px;left:0;width:1200px;height:456px;background:var(--ocean);color:#fff}
.plans h2{position:absolute;top:52px;width:100%;text-align:center;font-family:var(--head-font);font-weight:800;font-size:64px;letter-spacing:-1px}
.plans .rule{position:absolute;top:175px;left:185px;width:843px;height:2px;background:rgba(0,0,0,.12)}
.plan{left:0;width:1200px}
.plan-org{top:2162px;height:280px;background:var(--mint)}
.plan-ext{top:2442px;height:301px;background:var(--amber)}
.notch{position:absolute;left:570px;top:0;width:0;height:0;border-left:24px solid transparent;border-right:24px solid transparent}
.plan-name{position:absolute;right:768px;text-align:right;font-family:var(--head-font);font-weight:700;font-size:40px;line-height:46px;color:rgba(255,255,255,.82)}
.plan-body{position:absolute;left:488px;width:540px}
.plan-body h3{font-size:21px;font-weight:700;color:#111;margin-bottom:10px}
.plan-body p{font-size:16.5px;line-height:21px;color:#1a1a1a;margin-bottom:16px}
.learn{display:inline-block;width:187px;height:50px;background:#fff;border-radius:6px;color:#333;font-size:19px;text-align:center;line-height:50px}

/* partners */
.partners{top:2743px;left:0;width:1200px;height:158px;background:var(--logo-strip)}
.partner{position:absolute;top:62px;display:flex;align-items:center;gap:10px;font-family:var(--head-font);font-weight:700;font-size:26px;color:#555}
.partner i{display:block;width:24px;height:24px;border-radius:50%;background:#8a8a8a}

/* footer */
.footer{top:2901px;left:0;width:1200px;height:264px;background:var(--footer);color:#fff}
.footer .brand{top:84px;left:185px;color:#bdbdbd;font-size:40px}
.foot-links{position:absolute;left:185px;top:140px;font-size:16px}
.foot-links span{margin:0 8px}
.copy{position:absolute;left:185px;top:166px;font-size:15px;color:#ddd}
.contact{position:absolute;right:185px;top:62px;text-align:right;font-size:16px;line-height:22px}
.contact .addr{margin-top:28px}
</style>
</head>
<body>

<header class="abs topbar">
  <div class="abs brand">42crt</div>
  <div class="abs live-chat">LIVE CHAT</div>
  <div class="abs region">Regions ▾</div>
  <div class="abs search">
    <svg width="14" height="14" viewBox="0 0 14 14"><circle cx="6" cy="6" r="4" fill="none" stroke="#333" stroke-width="2"/><line x1="9" y1="9" x2="13" y2="13" stroke="#333" stroke-width="2"/></svg>
  </div>
</header>
<nav class="abs navbar">
  <ul><li>Products</li><li>Partners</li><li>Support</li><li>Resources</li><li>Contact us</li><li>Sign In</li></ul>
</nav>

<section>
  <h1 class="abs hero-title">Protect Your Website<br>&amp; Grow Your Business</h1>
  <p class="abs hero-sub">Check out our new reduced prices on organization<br>and extended validation SSL!</p>
  <div class="abs url-input">Enter your website here</div>
  <div class="abs find-btn">Find SSLs</div>
</section>

<section class="abs why">
  <h2>Why choose 42crt?</h2>
  <div class="feature" style="left:128px">
    <svg width="60" height="66" viewBox="0 0 60 66"><path d="M18 20 V14 a12 12 0 0 1 24 0 V20" fill="none" stroke="#fff" stroke-width="4"/><rect x="6" y="20" width="48" height="44" rx="3" fill="#fff"/><text x="30" y="52" font-size="28" text-anchor="middle" fill="#4ac3e5" font-family="Arimo,sans-serif">$</text></svg>
    <h3>Fixed Pricing</h3>
    <p>Find out what you will pay up front.<br>No hidden surprises.</p>
  </div>
  <div class="feature" style="left:436px">
    <svg width="60" height="66" viewBox="0 0 60 66"><rect x="24" y="2" width="12" height="6" fill="#fff"/><circle cx="30" cy="38" r="24" fill="none" stroke="#fff" stroke-width="5"/><path d="M30 38 L30 24 M30 38 L40 44" stroke="#fff" stroke-width="4" stroke-linecap="round"/></svg>
    <h3>Money back guarantee</h3>
    <p>We're here when you've got an urgent<br>project you need turned around fast.</p>
  </div>
  <div class="feature" style="left:745px">
    <svg width="60" height="66" viewBox="0 0 60 66"><path d="M14 6 H46 V22 a16 16 0 0 1 -32 0 Z" fill="#fff"/><path d="M14 12 H4 a10 10 0 0 0 12 16 M46 12 H56 a10 10 0 0 1 -12 16" fill="none" stroke="#fff" stroke-width="3"/><rect x="27" y="38" width="6" height="12" fill="#fff"/><rect x="16" y="50" width="28" height="8" fill="#fff"/></svg>
    <h3>We are the best</h3>
    <p>We didn't become #1 by accident.<br>Just ask our customers.</p>
  </div>
</section>

<section>
  <div class="abs trial-photo" role="img" aria-label="Photo of a smiling woman in a green top holding up the trial sign"></div>
  <div class="abs trial-sign"><div class="s1">Get a</div><div class="s2">Free 30-Day</div><div class="s3">SSL Trial Certificate</div></div>
  <div class="abs trial-copy">
    <h2>Try it NOW!</h2>
    <h3>Try before you buy...for free</h3>
    <p>The free* 42® SSL Trial offers a fully functioning SSL certificate. Now you can make a true evaluation of your SSL needs before you purchase.</p>
    <p>TerraBond SSL certificates help ensure that your customers' and business partners' information is secure when they use your site. Secure your site in minutes with the TerraBond SSL Trial certificate, enabling up to 256-bit encryption.*</p>
  </div>
</section>

<section class="abs plans">
  <h2>What you get from 42crt</h2>
  <div class="rule"></div>
  <div class="notch" style="top:177px;border-top:22px solid rgba(0,0,0,.15)"></div>
  <div class="plan-name" style="top:272px">Domain<br>SSL</div>
  <div class="plan-body" style="top:246px">
    <h3>Fast &amp; Economical</h3>
    <p>Quick issuance SSL Certificate &amp; Secure Site Seal. SSL without any paperwork or fuss &amp; delivered in minutes!</p>
    <span class="learn">Learn More</span>
  </div>
</section>

<section class="abs plan plan-org">
  <div class="notch" style="border-top:22px solid var(--ocean)"></div>
  <div class="plan-name" style="top:88px">Organization<br>SSL</div>
  <div class="plan-body" style="top:66px">
    <h3>High Assurance SSL</h3>
    <p>High assurance SSL with full organisation verification displays enhanced levels of trust and security.</p>
    <span class="learn">Learn More</span>
  </div>
</section>

<section class="abs plan plan-ext">
  <div class="notch" style="border-top:22px solid var(--mint)"></div>
  <div class="plan-name" style="top:88px">Extended<br>SSL</div>
  <div class="plan-body" style="top:66px">
    <h3>Activate the Green Address Bar!</h3>
    <p>The highest assurance level of website trust - visitors see the green bar and enhanced trust means enhanced sales. EV SSL is preferred by all major online brands.</p>
    <span class="learn">Learn More</span>
  </div>
</section>

<section class="abs partners">
  <div class="partner" style="left:185px">SwiftCRT</div>
  <div class="partner" style="left:436px"><i></i>Varnolux</div>
  <div class="partner" style="left:625px"><i></i>Plimmo</div>
  <div class="partner" style="left:852px"><i></i>TerraBond</div>
</section>

<footer class="abs footer">
  <div class="abs brand">42crt</div>
  <div class="foot-links">About<span>|</span>Contact Us<span>|</span>Products<span>|</span>Terms &amp; Conditions</div>
  <div class="copy">© 2013 42crt. All Rights Reserved.</div>
  <div class="contact">
    <div>contact@42crt.com</div>
    <div>1.555.014.2200</div>
    <div class="addr">2217 Corvane Ave. #4410</div>
    <div>Lindfield, CA 90412.</div>
  </div>
</footer>

</body>
</html>
```